Web Design Project

Parallel Press owns and operates a large number of editorial websites. These websites provides mostly consumers in the financial services space with information and price comparisons for a particular service.

Parallel Press, as the holding company for each of these sites, currently has no website. We need to build a website targeted towards potential partners for our websites. The idea being that when we start a conversation with a partner, they can view our site and obtain some basic information about who we are.

The structure of the site is to be very simple, containing only a brief description about who we are, our contact details and a list of some of our websites:
• LifeCoverHub.net.au
• MotorCoverCheckers.com.au
• HouseCoverCheckers.com.au
• MedicalCoverCheckers.com.au
• LivingCoverCheckers.com.au
• TripCoverCheckers.com.au
• AnimalCoverCheckers.com.au
• PrivateCreditCheckers.com.au
• MobileCoolingUnit.com.au
• FixedSavingYield.com.au
• ThriftyDays.com.au
• CashNana.com.au
• TameThePlastic.com.au
• PurseKeeper.com.au
• ThirdPartyClaimsCoverOz.com.au
• Trade-Protection.com.au
• MotorCoverProviders.com.au
• MedicalCoverProviders.com.au
• HouseCoverDownUnder.com
• LivingCoverDownUnder.com
• SalaryShieldCoverDownUnder.com
• MedicalCoverDownUnder.com
• AnimalCoverDownUnder.com
• PrivateCreditDownUnder.com
• PlasticPaysDownUnder.com
• HouseFinanceDownUnder.com
• RetireFundHub.net.au

The design of the site should say 'Internet company', 'professional', 'fresh thinking'. The design should not look like a corporate site that you would see from any corporate services business with images of people in suits. We are ultimately an Internet business and there should be a unique feel to the site.

We are open to a suggestion of a colour pallet as the holding company does not have an established logo.

Some sites that we like are:

http://www.brindle-studio.example/#home
http://preview11.layoutvault.example/wt_48261/index.html
http://preview11.layoutvault.example/wordpress_59134/
http://mulloptic.example/
http://www.tandrel.example/
http://www.kovasilindqvist.example/
http://www.sharpsitegallery.example/Corporate/design-ideas-detail.html?id=4172
http://brackenway.example/
http://oskarteel.example/

Reason: Hi all, Apologies, but I need to extend the timeline. One of our key stakeholders is away for the next week. There are a few good designs that we have received to date and there are some tweaks that we would like to see before making a final decision. Thank you to everyone that has submitted designs - Have a great new year. Bram

Reason: Sorry to have to delay the deadline on this, but we did not find anything in the designs really resonated with us. We will have a further think about the existing designs that have been submitted and how we can provide more specific feedback to the designers to make some modifications to the designs.

Target Market(s)

We are targeting insurance companies / brokers that we are talking to. The idea is that we show a professional face to them.

Industry/Entity Type

Financial

Requirements
Must have
• Home Page (possibly integrated with About us details)
Contact Us
Our Sites

```html
<!DOCTYPE html>
<html lang="en">
<head>
<meta charset="utf-8">
<title>Parallel Press</title>
<link rel="stylesheet" href="https://fonts.googleapis.com/css2?family=Anton&family=Noto+Sans:wght@400;700&display=swap">
<style>
  :root {
    --brand-navy: #033a6b;
    --top-strip: #02335f;
    --sky-top: #1490f5;
    --sky-bottom: #d4ecfb;
    --sea-top: #04519a;
    --sea-bottom: #001a33;
    --berg-light: #e8f4fd;
    --berg-blue: #1a6ab5;
    --logo-gold: #f2a900;
    --headline-blue: #0a5aa8;
    --white: #ffffff;
    --nav-muted: #bfe0fb;
    --accent-orange: #f26b3a;
    --accent-orange-dark: #d9521f;
    --sign-blue: #0b63ad;
    --button-blue: #1a92d6;
    --button-blue-dark: #0b74b6;
    --body-grey: #666666;
    --label-grey: #333333;
    --field-fill: #f3f3f3;
    --field-border: #cccccc;
    --rule: #c8c8c8;
    --footer-top: #03223d;
    --footer-bottom: #000a14;
  }
  * { box-sizing: border-box; margin: 0; padding: 0; }
  html, body { width: 1012px; height: 1200px; overflow: hidden; }
  body {
    position: relative;
    background: var(--white);
    font-family: "Noto Sans", Verdana, sans-serif;
  }

  /* Hero */
  .hero {
    position: absolute; left: 0; top: 0; width: 1012px; height: 708px;
    background:
      linear-gradient(to bottom, var(--sky-top) 0, var(--sky-bottom) 284px, transparent 284px),
      radial-gradient(ellipse 420px 360px at 500px 420px, #0a5fae 0%, transparent 70%),
      linear-gradient(to bottom, var(--sea-top) 284px, #033f7a 480px, var(--sea-bottom) 708px);
    overflow: hidden;
  }
  .top-strip { position: absolute; left: 0; top: 0; width: 1012px; height: 15px; background: var(--top-strip); }
  .logo-box {
    position: absolute; left: 30px; top: 0; width: 268px; height: 71px;
    background: var(--brand-navy);
    display: flex; align-items: center; justify-content: center;
  }
  .logo-name {
    font-family: "Anton", Impact, sans-serif;
    font-size: 33px; letter-spacing: 0.5px; color: var(--logo-gold);
  }
  .main-nav { position: absolute; left: 44px; top: 73px; display: flex; gap: 32px; }
  .main-nav a {
    font-family: Arial, "Noto Sans", sans-serif;
    font-size: 15px; color: var(--nav-muted); text-decoration: none;
  }
  .main-nav a.is-current { color: var(--white); }

  .hero-copy { position: absolute; left: 45px; top: 250px; font-family: "Anton", Impact, sans-serif; }
  .hero-kicker { font-size: 26px; line-height: 30px; color: var(--headline-blue); letter-spacing: 0.2px; }
  .hero-word { font-size: 86px; line-height: 84px; color: var(--white); margin-top: 2px; letter-spacing: 0.5px; }
  .hero-sub { font-size: 26px; line-height: 30px; color: var(--white); margin-top: -2px; }

  .iceberg-art {
    position: absolute; left: 478px; top: 163px; width: 500px; height: 502px;
    background: linear-gradient(to bottom, var(--berg-light) 0%, #9fd0f2 24%, var(--berg-blue) 27%, #0d4f8e 70%, #0a5ba6 100%);
    border-radius: 46% 46% 30% 30% / 30% 30% 22% 22%;
    opacity: 0.85;
  }
  .whale-art {
    position: absolute; left: 298px; top: 410px; width: 134px; height: 90px;
    background: radial-gradient(ellipse at center, #0d355f 0%, rgba(13,53,95,0.4) 60%, transparent 75%);
  }

  /* Content */
  .about { position: absolute; left: 46px; top: 745px; width: 461px; }
  .about-text { font-size: 17.5px; line-height: 20.3px; color: var(--body-grey); }
  .about-text + .about-text { margin-top: 20px; }
  .about-name { font-size: 25px; color: var(--accent-orange); margin-right: 8px; }

  .signup { position: absolute; left: 563px; top: 742px; width: 415px; }
  .signup-title { font-size: 26px; line-height: 34px; font-weight: 400; color: var(--sign-blue); margin-bottom: 8px; }
  .field-label { display: block; font-size: 11.5px; color: var(--label-grey); margin-bottom: 3px; }
  .field-input, .field-message {
    display: block; width: 260px; height: 26px;
    background: var(--field-fill); border: 1px solid var(--field-border);
    margin-bottom: 8px; font: inherit;
  }
  .field-message { width: 415px; height: 109px; resize: none; }

  .rule { position: absolute; top: 1044px; height: 1px; background: var(--rule); }
  .rule-left { left: 46px; width: 461px; }
  .rule-right { left: 563px; width: 416px; }

  .button {
    position: absolute; top: 1060px; height: 24px;
    display: flex; align-items: center; justify-content: center;
    font-size: 11.5px; font-weight: 700; color: var(--white); text-decoration: none;
    border-radius: 4px; letter-spacing: 0.2px;
  }
  .button-directory { left: 348px; width: 148px; background: linear-gradient(var(--accent-orange), var(--accent-orange-dark)); }
  .button-signup { left: 892px; width: 77px; background: linear-gradient(var(--button-blue), var(--button-blue-dark)); border: none; font-family: inherit; }

  /* Footer */
  .site-footer {
    position: absolute; left: 0; top: 1139px; width: 1012px; height: 61px;
    background: linear-gradient(var(--footer-top), var(--footer-bottom));
  }
  .footer-note { position: absolute; left: 43px; top: 20px; font-size: 13.5px; color: var(--white); }
</style>
</head>
<body>
  <header class="hero">
    <div class="top-strip"></div>
    <div class="logo-box"><span class="logo-name">Parallel Press</span></div>
    <nav class="main-nav">
      <a href="#" class="is-current">Home</a>
      <a href="#">Our Sites</a>
      <a href="#">Contact Us</a>
    </nav>
    <div class="hero-copy">
      <p class="hero-kicker">WE HELP YOUR CUSTOMERS</p>
      <p class="hero-word">DISCOVER</p>
      <p class="hero-sub">MORE ABOUT YOUR BUSINESS</p>
    </div>
    <div class="whale-art" role="img" aria-label="Illustration of a whale swimming beneath the surface"></div>
    <div class="iceberg-art" role="img" aria-label="Illustration of an iceberg with its large hidden mass below the waterline"></div>
  </header>

  <main>
    <section class="about">
      <p class="about-text"><span class="about-name">Parallel Press</span>is an Australian-based internet marketing company. We specialise in attracting customers from our directory of more than 100 sites to our network of trusted partners. Our skill lies in generating targeted traffic to our range of web sites and identifying the right partners for each of the sites, ensuring that the visitors to our sites get what they are looking for.</p>
      <p class="about-text">If you are interested in partnering with us on one or multiple of our sites, please contact us.</p>
    </section>
    <div class="rule rule-left"></div>
    <a href="#" class="button button-directory">View Our Directory</a>

    <form class="signup">
      <h2 class="signup-title">Partner Sign-up</h2>
      <label class="field-label" for="contact-name">Contact Name</label>
      <input class="field-input" id="contact-name" type="text">
      <label class="field-label" for="contact-email">Contact E-mail</label>
      <input class="field-input" id="contact-email" type="email">
      <label class="field-label" for="message">Message</label>
      <textarea class="field-message" id="message"></textarea>
    </form>
    <div class="rule rule-right"></div>
    <button class="button button-signup" type="button">Sign-up</button>
  </main>

  <footer class="site-footer">
    <p class="footer-note">© 2012 Parallel Press</p>
  </footer>
</body>
</html>
```